Flyer for the Harvest Lantern Gathering 2018

Design a flyer for our annual conference with basic information about the conference: conference logo and year,

Location:
Dunmore Community Center (Downtown Portland)
482 Willowby Street, Portland, ME 04117,

Date:
August 24th, 25th and 26th, 2018
Start time 6:00PM

I would like the following three words added to the flyer. These words describe the vision of the conference:
Prophetic, Worship, Prayer

```html
<!DOCTYPE html>
<html lang="en">
<head>
<meta charset="utf-8">
<title>Harvest Lantern Gathering 2018 — Flyer</title>
<link rel="stylesheet" href="https://fonts.googleapis.com/css2?family=Russo+One&family=PT+Sans:wght@700&display=swap">
<style>
  :root {
    --frame: #231f20;
    --paper: #ffffff;
    --ink: #231f20;
    --accent: #f07a22;
    --band-red: #e52d27;
    --band-orange: #ef7d24;
    --fire-yellow: #f9df2c;
    --fire-orange: #f3952a;
    --fire-red: #ec4a26;
    --shadow-grey: #b5b5b5;
  }
  html, body {
    margin: 0;
    padding: 0;
    width: 1200px;
    height: 937px;
    overflow: hidden;
    background: var(--frame);
  }
  .flyer {
    position: relative;
    width: 1200px;
    height: 937px;
    background: var(--frame);
  }
  .flyer-card {
    position: absolute;
    left: 50px;
    top: 42px;
    width: 1100px;
    height: 852px;
    background: var(--paper);
    overflow: hidden;
  }
  .flyer-art {
    position: absolute;
    inset: 0;
  }
  .headline text {
    font-family: "Russo One", sans-serif;
    fill: var(--ink);
  }
  .vision-words {
    font-family: "Russo One", sans-serif;
    fill: #ffffff;
  }
  .details {
    position: absolute;
    left: 76px;
    top: 578px;
    font-family: "PT Sans", sans-serif;
    color: var(--ink);
  }
  .details-label {
    margin: 0;
    font-family: "Russo One", sans-serif;
    font-size: 31px;
    line-height: 1;
    color: var(--accent);
    letter-spacing: 0.5px;
  }
  .details-text {
    margin: 8px 0 16px;
    font-size: 23.5px;
    line-height: 30px;
    font-weight: 700;
  }
  .event-mark {
    position: absolute;
    left: 770px;
    top: 570px;
    width: 260px;
    text-align: center;
  }
  .event-mark-dot {
    display: block;
    width: 170px;
    height: 170px;
    margin: 0 auto 22px;
    border-radius: 50%;
    border: 4px solid var(--accent);
    box-sizing: border-box;
  }
  .event-mark-name {
    font-family: "Russo One", sans-serif;
    font-size: 36px;
    line-height: 1;
    color: var(--ink);
    letter-spacing: 1px;
  }
</style>
</head>
<body>
<main class="flyer">
  <section class="flyer-card">
    <svg class="flyer-art" width="1100" height="852" viewBox="0 0 1100 852">
      <defs>
        <radialGradient id="fireGlow" cx="834" cy="470" r="900" gradientUnits="userSpaceOnUse">
          <stop offset="0" stop-color="var(--fire-yellow)"/>
          <stop offset="0.35" stop-color="var(--fire-orange)"/>
          <stop offset="0.8" stop-color="var(--fire-red)"/>
        </radialGradient>
        <linearGradient id="topBand" x1="0" y1="0" x2="1" y2="0">
          <stop offset="0" stop-color="var(--band-red)"/>
          <stop offset="1" stop-color="var(--band-orange)"/>
        </linearGradient>
      </defs>

      <!-- soft shadow under the wave -->
      <path d="M0,344 C250,380 560,540 834,494 C910,484 1000,552 1100,584" fill="none" stroke="#dcdcdc" stroke-width="34"/>
      <path d="M0,330 C250,366 560,526 834,480 C910,470 1000,538 1100,570" fill="none" stroke="var(--shadow-grey)" stroke-width="18"/>

      <!-- flame field -->
      <path d="M0,0 H1100 V550 C1000,518 900,460 834,470 C560,478 250,320 0,278 Z" fill="url(#fireGlow)"/>
      <rect x="0" y="0" width="1100" height="108" fill="url(#topBand)" opacity="0.9"/>

      <text class="vision-words" x="558" y="86" font-size="49" text-anchor="middle" textLength="980" lengthAdjust="spacingAndGlyphs">PROPHETIC | WORSHIP | PRAYER</text>

      <g class="headline">
        <text x="1050" y="202" font-size="100" text-anchor="end" textLength="700" lengthAdjust="spacingAndGlyphs">HARVEST</text>
        <text x="1050" y="338" font-size="160" text-anchor="end" textLength="732" lengthAdjust="spacingAndGlyphs">LANTERN</text>
        <text x="1050" y="418" font-size="78" text-anchor="end" textLength="640" lengthAdjust="spacingAndGlyphs">GATHERING</text>
        <text x="1050" y="478" font-size="56" text-anchor="end">2018</text>
      </g>
    </svg>

    <div class="details">
      <h2 class="details-label">LOCATION:</h2>
      <p class="details-text">Dunmore Community Center (Downtown Portland)<br>482 Willowby Street, Portland, ME 04117</p>
      <h2 class="details-label">DATE:</h2>
      <p class="details-text">August 24th, 25th &amp; 26th, 2018<br>Start time 6:00PM</p>
    </div>

    <div class="event-mark">
      <span class="event-mark-dot"></span>
      <div class="event-mark-name">LANTERNCON</div>
    </div>
  </section>
</main>
</body>
</html>
```